Website Monitoring Business Needs a Single Page Website Design

I need a website design for a new web based service called TallyNest. This service checks to see if a website is up or down and how quickly or slowly it is responding. Users sign up for a small monthly fee and add one or more websites to monitor based on the plan they purchase. I prefer a single page design.

There will be 3 pricing plans to start with. A free plan and then 2 paid plans. The pricing plans should be included on the single page.

Here are four close competitors to what this product will offer:

https://www.vorbelix.com/
http://quellarind.com/
https://www.marbotrix.com/
https://www.dune58kq.com/

Target Market(s)

Website owners, bloggers

Industry/Entity Type

Business

Coding

Coded - Design and coding required

Number of Pages Required

1 page

Font styles to use
Sans Serif

Requirements
Must have
• Responsive design
Nice to have
• Parallax scrolling

```html
<!DOCTYPE html>
<html lang="en">
<head>
<meta charset="utf-8">
<title>TallyNest – Website Monitoring</title>
<link href="https://fonts.googleapis.com/css2?family=Oxygen:wght@300;400;700&family=PT+Sans:wght@400;700&family=Roboto:wght@300;400;500;700&display=swap" rel="stylesheet">
<style>
:root{
  --yellow:#f4cb1c;
  --yellow-dark:#e0b90f;
  --ink:#222222;
  --ink-soft:#2b2b2b;
  --black:#050505;
  --grey-text:#7d7d7d;
  --card-bg:#f3f3f3;
  --line:#dcdcdc;
  --white:#ffffff;
}
*{box-sizing:border-box;margin:0;padding:0}
html,body{width:1200px;height:3358px;overflow:hidden}
body{position:relative;background:var(--white);font-family:"Oxygen",Arial,sans-serif;color:var(--ink)}
section,header,footer{position:absolute;left:0;width:1200px}

/* Hero */
.hero{top:0;height:649px;overflow:hidden}
.hero-photo{position:absolute;inset:0;background:linear-gradient(180deg,#3a4550 0%,#2c3640 40%,#46525c 70%,#2a3038 100%)}
.hero-shade{position:absolute;inset:0;background:rgba(15,18,22,.45)}
.topbar{position:absolute;top:0;left:0;width:1200px;height:135px;background:linear-gradient(180deg,rgba(0,0,0,.55),rgba(0,0,0,0))}
.brand{position:absolute;left:100px;top:42px;font-family:"PT Sans",sans-serif;font-weight:700;font-size:40px;color:var(--yellow)}
.nav{position:absolute;top:58px;left:555px;display:flex;font-family:"Roboto",sans-serif;font-size:13px;font-weight:500;color:var(--white);letter-spacing:.3px}
.nav span{padding:0 11px;border-left:1px solid rgba(255,255,255,.7);line-height:14px}
.nav span:first-child{border-left:0;padding-left:0}
.btn-login,.btn-signup{position:absolute;top:46px;height:40px;font-family:"Roboto",sans-serif;font-size:13px;font-weight:500;display:flex;align-items:center;justify-content:center}
.btn-login{left:956px;width:66px;border:1.5px solid var(--white);color:var(--white)}
.btn-signup{left:1035px;width:66px;background:var(--yellow);color:var(--ink)}
.hero-kicker{position:absolute;top:250px;width:100%;text-align:center;font-size:33px;font-weight:700;color:var(--yellow)}
.hero-title{position:absolute;top:308px;width:100%;text-align:center;font-size:30px;line-height:44px;font-weight:700;color:var(--white)}
.hero-btn{position:absolute;top:443px;height:48px;font-family:"Roboto",sans-serif;font-size:15px;font-weight:700;display:flex;align-items:center;justify-content:center;letter-spacing:.3px}
.hero-btn.outline{left:340px;width:240px;border:2px solid var(--white);color:var(--white)}
.hero-btn.solid{left:647px;width:240px;background:var(--yellow);color:var(--ink)}

/* Intro */
.intro{top:649px;height:643px}
.intro-text{position:absolute;left:220px;top:50px;width:760px;text-align:center;font-family:"Roboto",sans-serif;font-weight:300;font-size:13.5px;line-height:22px;color:var(--grey-text)}
.intro-text p+p{margin-top:12px}
.video{position:absolute;left:320px;top:226px;width:569px;height:372px;background:#2a2d2b}
.video-name{position:absolute;top:140px;width:100%;text-align:center;font-family:"PT Sans",sans-serif;font-weight:700;font-size:44px;color:#8c7a2a}
.video-controls{position:absolute;left:0;bottom:0;width:100%;height:46px;background:#1c1d1c}

/* Features */
.features{top:1292px;height:557px;overflow:hidden}
.features-photo{position:absolute;inset:0;background:linear-gradient(120deg,#1e2124 0%,#3a3e42 45%,#2a2d30 70%,#141618 100%)}
.features-shade{position:absolute;inset:0;background:rgba(0,0,0,.35)}
.section-title{position:absolute;width:100%;text-align:center;font-size:34px;font-weight:700}
.features .section-title{top:46px;color:var(--white)}
.feature{position:absolute;top:148px;width:210px;text-align:center;color:var(--white)}
.feature-icon{display:block;margin:0 auto}
.feature h3{margin-top:22px;font-family:"Roboto",sans-serif;font-size:14px;font-weight:700;letter-spacing:.3px}
.feature p{margin-top:12px;font-family:"Roboto",sans-serif;font-size:12px;line-height:17px;color:#e8e8e8}

/* Pricing */
.pricing{top:1849px;height:784px}
.pricing .section-title{top:44px;font-weight:400;color:var(--ink)}
.plan{position:absolute;top:150px;width:300px;height:576px;background:var(--card-bg);box-shadow:0 0 3px rgba(0,0,0,.12)}
.plan-head{height:201px;background:var(--yellow);text-align:center;color:var(--ink);padding-top:24px}
.plan.free .plan-head{background:var(--ink);color:var(--white)}
.plan-name{font-family:"Roboto",sans-serif;font-size:25px;font-weight:400}
.plan-sub{font-family:"Roboto",sans-serif;font-size:12px;color:#8a6f00;margin-top:2px}
.plan.free .plan-sub{color:#bbb}
.plan-price{margin-top:26px;display:flex;align-items:baseline;justify-content:center;font-family:"Roboto",sans-serif}
.plan-price .cur{font-size:30px;font-weight:700;margin-right:4px}
.plan-price .amt{font-size:58px;font-weight:700;line-height:1}
.plan-price .per{font-size:14px;font-weight:500;margin-left:12px}
.plan-list{list-style:none;width:210px;margin:22px auto 0;font-family:"Roboto",sans-serif;font-size:12.5px;color:#444;text-align:center}
.plan-list li{height:42px;line-height:42px;border-bottom:1px solid var(--line)}
.plan-btn{position:absolute;left:64px;top:520px;width:172px;height:38px;background:var(--yellow);font-family:"Roboto",sans-serif;font-size:13px;font-weight:700;display:flex;align-items:center;justify-content:center;color:var(--ink)}
.plan.free .plan-btn{background:var(--ink);color:var(--white)}

/* Clients */
.clients{top:2633px;height:305px;background:var(--ink-soft)}
.clients-title{position:absolute;top:34px;width:100%;text-align:center;font-size:27px;font-weight:300;color:#d9d9d9}
.client{position:absolute;top:110px;width:170px;height:125px;border:1.5px solid #5c5c5c;display:flex;align-items:center;justify-content:center;font-family:"Oxygen",sans-serif;font-size:22px;font-weight:700;color:#a9a9a9}

/* Footer */
.footer-links{top:2938px;height:286px;background:var(--black)}
.footer-col{position:absolute;top:56px;font-family:"Roboto",sans-serif;color:var(--white)}
.footer-col h4{font-size:12px;font-weight:700;letter-spacing:.5px;margin-bottom:28px}
.footer-col ul{list-style:none;font-size:11px;line-height:18px;color:#e6e6e6}
.footer-bar{top:3224px;height:134px;background:#1c1c1c}
.social{position:absolute;left:146px;top:58px;display:flex;gap:6px}
.social span{height:30px;padding:0 8px;background:#3a3a3a;color:#e6e6e6;font-family:"Roboto",sans-serif;font-size:11px;display:flex;align-items:center}
.copyright{position:absolute;left:844px;top:66px;font-family:"Roboto",sans-serif;font-size:11px;color:#e6e6e6}
</style>
</head>
<body>

<header class="hero">
  <div class="hero-photo" role="img" aria-label="Photo of an operator at a monitoring control desk with several screens"></div>
  <div class="hero-shade"></div>
  <div class="topbar"></div>
  <div class="brand">TallyNest</div>
  <nav class="nav"><span>PRODUCT</span><span>PRICING</span><span>RESOURCES</span><span>WHY TALLYNEST</span></nav>
  <div class="btn-login">LOG IN</div>
  <div class="btn-signup">SIGN UP</div>
  <h2 class="hero-kicker">Downtime Happens. Get Notified!</h2>
  <h1 class="hero-title">TallyNest monitors your websites every<br>minute and alerts you if your sites are down.</h1>
  <div class="hero-btn outline">START MONITORING NOW</div>
  <div class="hero-btn solid">VIEW OUR PLANS</div>
</header>

<section class="intro">
  <div class="intro-text">
    <p>Anyone with a website knows that things can sometimes go wrong. Sometimes it is with the code, the server or the network. TallyNest monitors your websites every minute and alerts you if your sites are down.</p>
    <p>A website can be down in various ways. It could be unreachable indicating a network problem, it could be up but throwing some sort of an error, or it could be misconfigured and not serving the correct content. Whatever the issue, TallyNest will identify it for you.</p>
  </div>
  <div class="video">
    <div class="video-name">TallyNest</div>
    <svg style="position:absolute;left:236px;top:108px" width="110" height="110" viewBox="0 0 110 110">
      <circle cx="55" cy="55" r="49" fill="rgba(255,255,255,.08)" stroke="#bdbdbd" stroke-width="7"/>
      <path d="M43 32 L78 55 L43 78 Z" fill="#cfcfcf"/>
    </svg>
    <div class="video-controls">
      <svg width="569" height="46" viewBox="0 0 569 46">
        <path d="M16 13 L30 23 L16 33 Z" fill="#f4cb1c"/>
        <rect x="44" y="13" width="4" height="20" fill="#fff"/><rect x="52" y="13" width="4" height="20" fill="#fff"/>
        <path d="M70 13 L80 23 L70 33 Z M80 13 L90 23 L80 33 Z" fill="#fff"/><rect x="91" y="13" width="3" height="20" fill="#fff"/>
        <rect x="124" y="21" width="285" height="4" fill="#666"/><rect x="124" y="21" width="102" height="4" fill="#fff"/>
        <circle cx="229" cy="23" r="6" fill="#fff"/>
        <text x="414" y="27" font-family="Roboto,sans-serif" font-size="11" fill="#fff">0:45 / 09:15</text>
        <path d="M494 19 h5 l6 -5 v18 l-6 -5 h-5 Z" fill="#fff"/>
        <path d="M527 14 h6 M527 14 v6 M553 14 h-6 M553 14 v6 M527 32 h6 M527 32 v-6 M553 32 h-6 M553 32 v-6" stroke="#fff" stroke-width="2.5" fill="none"/>
      </svg>
    </div>
  </div>
</section>

<section class="features">
  <div class="features-photo" role="img" aria-label="Photo of a technician working in a server room"></div>
  <div class="features-shade"></div>
  <h2 class="section-title">Features Overview</h2>

  <div class="feature" style="left:65px">
    <svg class="feature-icon" width="170" height="170" viewBox="0 0 170 170"><path d="M85 4 L166 85 L85 166 L4 85 Z" fill="#f4cb1c" stroke="#fff" stroke-width="3"/>
      <rect x="60" y="64" width="50" height="34" fill="none" stroke="#222" stroke-width="4"/><path d="M52 104 h66 l-6 7 h-54 Z" fill="#222"/><path d="M66 90 l10 -10 l8 6 l14 -14" stroke="#222" stroke-width="3" fill="none"/></svg>
    <h3>MONITORING</h3>
    <p>When your site is down it can mean lost sales, damage to your brand, and lower search engine rankings.</p>
  </div>
  <div class="feature" style="left:271px">
    <svg class="feature-icon" width="170" height="170" viewBox="0 0 170 170"><path d="M85 4 L166 85 L85 166 L4 85 Z" fill="#f4cb1c" stroke="#fff" stroke-width="3"/>
      <path d="M85 56 L114 108 H56 Z" fill="#222"/><rect x="82" y="72" width="6" height="20" fill="#f4cb1c"/><rect x="82" y="96" width="6" height="6" fill="#f4cb1c"/></svg>
    <h3>ALERTING</h3>
    <p>When your site is down you are immediately alerted. Get alerted via e-mail, SMS, Chirpline, push, Stackro, HubTalk, PageBell...</p>
  </div>
  <div class="feature" style="left:484px">
    <svg class="feature-icon" width="170" height="170" viewBox="0 0 170 170"><path d="M85 4 L166 85 L85 166 L4 85 Z" fill="#f4cb1c" stroke="#fff" stroke-width="3"/>
      <circle cx="85" cy="85" r="26" fill="none" stroke="#222" stroke-width="5"/><path d="M85 70 V86 H97" stroke="#222" stroke-width="5" fill="none"/></svg>
    <h3>STATS</h3>
    <p>View performance trends in a beautifully designed UI. View uptime, downtime and the and a breakdown of response ...</p>
  </div>
  <div class="feature" style="left:694px">
    <svg class="feature-icon" width="170" height="170" viewBox="0 0 170 170"><path d="M85 4 L166 85 L85 166 L4 85 Z" fill="#f4cb1c" stroke="#fff" stroke-width="3"/>
      <circle cx="85" cy="85" r="17" fill="none" stroke="#222" stroke-width="4"/><circle cx="85" cy="85" r="7" fill="none" stroke="#222" stroke-width="3"/>
      <path d="M85 60 v8 M85 102 v8 M60 85 h8 M102 85 h8 M67 67 l6 6 M97 97 l6 6 M103 67 l-6 6 M73 97 l-6 6" stroke="#222" stroke-width="6"/></svg>
    <h3>API</h3>
    <p>TallyNest provides an easy to use API for managing checks and integrating check results into your own application.</p>
  </div>
  <div class="feature" style="left:914px">
    <svg class="feature-icon" width="170" height="170" viewBox="0 0 170 170"><path d="M85 4 L166 85 L85 166 L4 85 Z" fill="#f4cb1c" stroke="#fff" stroke-width="3"/>
      <rect x="70" y="56" width="30" height="56" rx="5" fill="none" stroke="#222" stroke-width="4"/><circle cx="85" cy="104" r="3" fill="#222"/></svg>
    <h3>MOBILE</h3>
    <p>Managing your alerts and website checks with our mobile app couldn't be easier and you will be alerted where ever you.</p>
  </div>
</section>

<section class="pricing">
  <h2 class="section-title">Pricing Plans</h2>

  <div class="plan free" style="left:114px">
    <div class="plan-head">
      <div class="plan-name">Free Plan</div>
      <div class="plan-sub">...to start with</div>
      <div class="plan-price"><span class="cur">$</span><span class="amt">0</span><span class="per">/ Monthly</span></div>
    </div>
    <ul class="plan-list">
      <li>5 minutes monitoring intervals</li>
      <li>50 monitors</li>
      <li>No "Pro SMS" messages *</li>
      <li>2 months of logs</li>
    </ul>
    <div class="plan-btn">START FREE TRIAL</div>
  </div>

  <div class="plan" style="left:450px">
    <div class="plan-head">
      <div class="plan-name">Standard Plan</div>
      <div class="plan-sub">For Website and Server Monitoring</div>
      <div class="plan-price"><span class="cur">$</span><span class="amt">80</span><span class="per">/ Monthly</span></div>
    </div>
    <ul class="plan-list">
      <li>Includes 10 Websites</li>
      <li>1 min Poll Frequency</li>
      <li>Includes 1 Advanced Monitor</li>
      <li>100K RUM Pageviews</li>
      <li>Select 8 Test Locations</li>
      <li>50 SMS/Voice Credits Per Month</li>
    </ul>
    <div class="plan-btn">SIGN UP NOW</div>
  </div>

  <div class="plan" style="left:793px">
    <div class="plan-head">
      <div class="plan-name">Premium Plan</div>
      <div class="plan-sub">For Enterprises</div>
      <div class="plan-price"><span class="cur">$</span><span class="amt">220</span><span class="per">/ Monthly</span></div>
    </div>
    <ul class="plan-list">
      <li>Includes 300 Basic Monitors</li>
      <li>1 min Poll Frequency</li>
      <li>5M RUM Pageviews</li>
      <li>Select 16 Test Locations</li>
      <li>500 SMS/Voice Credits Per Month</li>
      <li>Premium Support</li>
    </ul>
    <div class="plan-btn">SIGN UP NOW</div>
  </div>
</section>

<section class="clients">
  <h2 class="clients-title">700,000+ Users Including These Fine Companies</h2>
  <div class="client" style="left:137px">Orchard</div>
  <div class="client" style="left:325px">Velnora</div>
  <div class="client" style="left:515px">Rivenmart</div>
  <div class="client" style="left:705px">Quarzic</div>
  <div class="client" style="left:891px">Halvex</div>
</section>

<footer class="footer-links">
  <div class="footer-col" style="left:146px"><h4>RESOURCES</h4><ul><li>API</li><li>Mobile Apps</li><li>Downloads</li><li>Tutorials</li><li>FAQ</li></ul></div>
  <div class="footer-col" style="left:311px"><h4>PRODUCT</h4><ul><li>Uptime</li><li>Performance</li><li>Transaction</li><li>Alerting</li><li>Page Speed</li><li>Pricing</li></ul></div>
  <div class="footer-col" style="left:472px"><h4>COMPANY</h4><ul><li>Why TallyNest</li><li>Contact</li><li>Brand Assets</li><li>Jobs</li><li>Customers</li><li>Affiliates</li></ul></div>
  <div class="footer-col" style="left:656px"><h4>SERVER MONITORING</h4><ul><li>Server Monitoring</li><li>Paneo Monitoring</li><li>Kernix Monitoring</li><li>Dune58kq Plugins</li><li>Webvane Monitoring</li><li>Tablix Monitoring</li></ul></div>
  <div class="footer-col" style="left:896px"><h4>WEBSITE MONITORING</h4><ul><li>Real User Monitoring</li><li>Web Page Analyzer</li><li>Synthetic Monitoring</li><li>Monitoring Locations</li><li>Mail Server Monitoring</li><li>DNS Monitoring</li></ul></div>
</footer>

<footer class="footer-bar">
  <div class="social"><span>Folio</span><span>Chirpline</span><span>Linkra</span><span>Viddo</span><span>Plusly</span></div>
  <div class="copyright">Copyright @ 2016. All rights reserved</div>
</footer>

</body>
</html>
```